Lantern Holdings Business Card

We are looking to design new business cards for our company. We have two office locations and would like to have both full addresses on the card. Each address needs two lines for the building name and street address and a line or two for the city, state and zip code. There should be a place for 2-3 phone numbers. The addresses and phone numbers are at the bottom of this description. We also need a place to put our company website and one email address. Our logo is attached.
We would like the card to be two sided. The back of the card should have a blue background with some part of our logo design on it. We would like the full logo on the front of the card as well. The front of the card should have a white background with the blue logo. We are open to listing our addresses on the front or the back of the card. The person who designed our logo gave us an excellent business card idea that we really liked. I have attached a picture of his business card idea so that we can build off of it.
Addresses:
The Marlow Exchange
2214 47th Street NW
Washington, DC 20419
Osprey Harbor Tower
815 Tamsin Boulevard #2207
Miami, FL 33987
Phone Numbers: (202) 555-0148
(202) 555-0193
Website: www.lanternholdings-example.com

```html
<!DOCTYPE html>
<html lang="en">
<head>
<meta charset="utf-8">
<title>Lantern Holdings Business Card</title>
<link rel="stylesheet" href="https://fonts.googleapis.com/css2?family=Open+Sans:wght@400;600&display=swap">
<style>
  :root {
    --brand-blue: #2b3379;
    --card-white: #ffffff;
    --backdrop: #d9d9d9;
    --text-light: #ffffff;
  }
  * { box-sizing: border-box; margin: 0; padding: 0; }
  html, body {
    width: 1200px;
    height: 900px;
    overflow: hidden;
    background: var(--backdrop);
    font-family: "Open Sans", Arial, sans-serif;
  }
  .canvas {
    width: 1200px;
    height: 900px;
    display: flex;
    flex-direction: column;
    align-items: center;
    justify-content: center;
    gap: 40px;
  }
  .card {
    width: 700px;
    height: 400px;
    position: relative;
    overflow: hidden;
    box-shadow: 0 6px 18px rgba(0,0,0,0.18);
  }
  .card--back {
    width: 560px;
    height: 320px;
    background: var(--brand-blue);
    display: flex;
    align-items: center;
    justify-content: center;
  }
  .card--front {
    background: var(--card-white);
  }
  .wordmark {
    display: flex;
    align-items: center;
    gap: 12px;
    text-transform: uppercase;
    font-weight: 400;
    letter-spacing: 0.06em;
    line-height: 1;
  }
  .wordmark__square {
    display: block;
    background: currentColor;
    border-radius: 4px;
  }
  .card--back .wordmark {
    color: var(--text-light);
    font-size: 30px;
  }
  .card--back .wordmark__square { width: 30px; height: 30px; }
  .front__brand {
    height: 235px;
    display: flex;
    flex-direction: column;
    align-items: center;
    justify-content: center;
    gap: 34px;
    padding-top: 14px;
  }
  .card--front .wordmark {
    color: var(--brand-blue);
    font-size: 46px;
  }
  .card--front .wordmark__square { width: 54px; height: 54px; }
  .website {
    color: var(--brand-blue);
    font-weight: 600;
    font-size: 18px;
  }
  .front__offices {
    position: absolute;
    left: 0;
    right: 0;
    bottom: 0;
    height: 165px;
    background: var(--brand-blue);
    color: var(--text-light);
    display: flex;
    align-items: center;
    justify-content: center;
    gap: 22px;
  }
  .office {
    font-style: normal;
    font-size: 16px;
    line-height: 1.4;
    width: 250px;
  }
  .office--miami { text-align: right; }
  .office--dc { text-align: left; }
  .office__divider {
    width: 2px;
    height: 94px;
    background: var(--text-light);
  }
</style>
</head>
<body>
  <main class="canvas">
    <section class="card card--back" aria-label="Card back">
      <div class="wordmark">
        <span class="wordmark__square" aria-hidden="true"></span>
        <span class="wordmark__name">Lantern Holdings</span>
      </div>
    </section>

    <section class="card card--front" aria-label="Card front">
      <div class="front__brand">
        <div class="wordmark">
          <span class="wordmark__square" aria-hidden="true"></span>
          <span class="wordmark__name">Lantern Holdings</span>
        </div>
        <p class="website">www.lanternholdings-example.com</p>
      </div>
      <div class="front__offices">
        <address class="office office--miami">
          Osprey Harbor Tower<br>
          815 Tamsin Boulevard #2207<br>
          Miami, FL 33987<br>
          (202) 555-0193
        </address>
        <span class="office__divider" aria-hidden="true"></span>
        <address class="office office--dc">
          The Marlow Exchange<br>
          2214 47th Street NW<br>
          Washington, DC 20419<br>
          (202) 555-0148
        </address>
      </div>
    </section>
  </main>
</body>
</html>
```